Math Tuition center needs a fresh website with LMS

I'm intending to buy a LMS theme for my wordpress site. But I need someone to help me design a few posters for the slider and set up the entire site for me. The LMS theme I'm eyeing has everything I need. But I don't have the time to figure things out.
I'm looking at either:
http://themes.brightmoss.com/tallyfield/
or
http://designkraal.org/zephor/
My current site is online at www.quorplex.com
I also need you to help me clear up the files I don't need on the server. So basically I need someone to design the new site for me, the LMS theme should make things easier but I'll need some customizations. I also need a webmaster who can help me set up the entire site so I don't have to turn on the widget or mess around with the theme.
Another thing, I have SEO done onsite so I can't change the contents, the meta-tags and such.
Industry/Entity Type
Online
Look and feel
Each slider illustrates characteristics of the customer's brand and the style your logo design should communicate.

```html
<!DOCTYPE html>
<html lang="en">
<head>
<meta charset="utf-8">
<title>quorplex Math Tuition</title>
<link rel="stylesheet" href="https://fonts.googleapis.com/css2?family=Montserrat:wght@400;600;700&family=Raleway:wght@400;500;600;700&display=swap">
<style>
  :root {
    --green: #6aad1f;
    --green-dark: #5a9618;
    --ink: #3d3d3d;
    --heading-grey: #6b6b6b;
    --body-grey: #8a8a8a;
    --nav-grey: #777777;
    --rule: #e8e8e8;
    --hero-pink: #fbeff0;
    --hero-grey: #ece8ea;
    --hero-lilac: #ddd3e2;
    --white: #ffffff;
  }
  * { margin: 0; padding: 0; box-sizing: border-box; }
  html, body { width: 1200px; height: 872px; overflow: hidden; background: var(--white); }
  body { position: relative; font-family: "Raleway", sans-serif; color: var(--ink); }

  .site-header {
    position: absolute; left: 0; top: 0; width: 1200px; height: 78px;
    border-bottom: 1px solid var(--rule); background: var(--white);
  }
  .brand {
    position: absolute; left: 72px; top: 22px;
    font-family: "Raleway", sans-serif; font-weight: 700; font-size: 30px;
    color: var(--green); letter-spacing: -0.5px;
  }
  .main-nav {
    position: absolute; top: 27px; left: 437px;
    display: flex; align-items: center;
    font-family: "Raleway", sans-serif; font-size: 11px; font-weight: 600;
    letter-spacing: 1.8px; color: var(--nav-grey); list-style: none;
  }
  .main-nav li { display: flex; align-items: center; white-space: nowrap; }
  .main-nav li + li::before {
    content: "·"; margin: 0 17px; color: #999; font-size: 14px;
  }
  .main-nav .is-current { color: #333; }

  .hero {
    position: absolute; left: 0; top: 93px; width: 1200px; height: 462px;
    background: var(--hero-pink); overflow: hidden;
  }
  .hero-photo {
    position: absolute; left: 0; top: 0; width: 1200px; height: 462px;
    background: linear-gradient(90deg, var(--hero-pink) 0%, var(--hero-pink) 30%, var(--hero-lilac) 60%, var(--hero-grey) 100%);
  }
  .hero-copy { position: absolute; left: 62px; top: 112px; }
  .hero-kicker {
    font-family: "Montserrat", sans-serif; font-weight: 400; font-size: 40px;
    color: var(--heading-grey); line-height: 1; letter-spacing: 1px;
  }
  .hero-title {
    margin-top: 6px;
    font-family: "Montserrat", sans-serif; font-weight: 700; font-size: 62px;
    color: var(--ink); line-height: 1; letter-spacing: 1px;
  }
  .hero-text {
    margin-top: 14px; width: 400px;
    font-family: "Montserrat", sans-serif; font-size: 17px; line-height: 22px; color: #555;
  }
  .hero-button {
    display: inline-block; margin-top: 12px; margin-left: 4px;
    width: 135px; height: 48px; line-height: 46px; text-align: center;
    background: var(--green); border-bottom: 3px solid var(--green-dark);
    color: var(--white); font-family: "Montserrat", sans-serif; font-weight: 700;
    font-size: 10px; letter-spacing: 2px; text-decoration: none;
  }

  .features {
    position: absolute; left: 70px; top: 623px;
    display: grid; grid-template-columns: repeat(4, 250px); column-gap: 21px;
  }
  .feature { width: 250px; text-align: center; }
  .feature-icon { display: block; margin: 0 auto; width: 48px; height: 48px; }
  .feature-title {
    margin-top: 44px; white-space: nowrap;
    font-family: "Montserrat", sans-serif; font-weight: 400; font-size: 14.5px; line-height: 18px;
    letter-spacing: 1.8px; color: #2e2e2e;
  }
  .feature-text {
    margin-top: 19px;
    font-family: "Montserrat", sans-serif; font-size: 13.3px; line-height: 22px; color: var(--body-grey);
  }
  .feature-text + .feature-text { margin-top: 22px; }
</style>
</head>
<body>
  <header class="site-header">
    <div class="brand">quorplex</div>
    <ul class="main-nav">
      <li class="is-current">HOME</li>
      <li>WHAT WE DO?</li>
      <li>NEWS</li>
      <li>TESTIMONIALS</li>
      <li>ABOUT OWEN</li>
      <li>CONTACT</li>
    </ul>
  </header>

  <section class="hero">
    <div class="hero-photo" role="img" aria-label="Photo of a student with headphones studying at a desk with a phone and an open book"></div>
    <div class="hero-copy">
      <p class="hero-kicker">RECORDED</p>
      <h1 class="hero-title">LESSONS</h1>
      <p class="hero-text">All our lessons are recorded so students can re-attend the lessons anytime they like.</p>
      <a class="hero-button" href="#">LEARN MORE</a>
    </div>
  </section>

  <section class="features">
    <article class="feature">
      <svg class="feature-icon" viewBox="0 0 48 48" aria-hidden="true">
        <circle cx="24" cy="24" r="24" fill="var(--green)"/>
        <circle cx="28" cy="18" r="6" fill="none" stroke="#fff" stroke-width="2.5"/>
        <path d="M18 35c0-6 4.5-9 10-9s10 3 10 9z" fill="none" stroke="#fff" stroke-width="2.5"/>
        <circle cx="19" cy="20" r="5" fill="#fff"/>
        <path d="M10 34c0-5 4-8 9-8 2 0 3 .4 4 1-3 2-4 4-4 7z" fill="#fff"/>
      </svg>
      <h2 class="feature-title">GROUP TUITION</h2>
      <p class="feature-text">quorplex Math Tuition by Owen Talbot offers A levels and O levels math tuition in small groups.</p>
      <p class="feature-text">Owen Talbot is a specialist in JC H2 math and O levels A math tuition. To</p>
    </article>
    <article class="feature">
      <svg class="feature-icon" viewBox="0 0 48 48" aria-hidden="true">
        <circle cx="24" cy="24" r="24" fill="var(--green)"/>
        <rect x="12" y="14" width="24" height="16" rx="1.5" fill="none" stroke="#fff" stroke-width="2.5"/>
        <rect x="22" y="30" width="4" height="4" fill="#fff"/>
        <rect x="17" y="34" width="14" height="2.5" fill="#fff"/>
      </svg>
      <h2 class="feature-title">BOARD-CASTS ON VIDSTREAM</h2>
      <p class="feature-text">Whiteboard broadcast, that's what Board-cast is all about. Owen painstakingly records his lessons into Board-casts and posts them on Vidstream for all to view for free.</p>
    </article>
    <article class="feature">
      <svg class="feature-icon" viewBox="0 0 48 48" aria-hidden="true">
        <circle cx="24" cy="24" r="24" fill="var(--green)"/>
        <rect x="15" y="12" width="18" height="24" fill="none" stroke="#fff" stroke-width="2.5"/>
        <path d="M20 12v13l3-2.5 3 2.5V12" fill="#fff"/>
        <line x1="18.5" y1="12" x2="18.5" y2="36" stroke="#fff" stroke-width="2"/>
      </svg>
      <h2 class="feature-title">MASTERY TUTORIAL</h2>
      <p class="feature-text">(coming soon)</p>
      <p class="feature-text">Nullam quis risus eget urna mollis ornare vel eu leo. Sed posuere consectetur est at lobortis.</p>
    </article>
    <article class="feature">
      <svg class="feature-icon" viewBox="0 0 48 48" aria-hidden="true">
        <circle cx="24" cy="24" r="24" fill="var(--green)"/>
        <circle cx="28" cy="18" r="6" fill="none" stroke="#fff" stroke-width="2.5"/>
        <path d="M18 35c0-6 4.5-9 10-9s10 3 10 9z" fill="none" stroke="#fff" stroke-width="2.5"/>
        <circle cx="19" cy="20" r="5" fill="#fff"/>
        <path d="M10 34c0-5 4-8 9-8 2 0 3 .4 4 1-3 2-4 4-4 7z" fill="#fff"/>
      </svg>
      <h2 class="feature-title">ULTRICIES EGESTA</h2>
      <p class="feature-text">Nullam quis risus eget urna mollis ornare vel eu leo. Sed posuere consectetur est at lobortis.</p>
    </article>
  </section>
</body>
</html>
```